New BROVANEL keyboard

We need to redesign the plastic cover of electronic keyboard. The equipment is a cooker with an agitation system. See page http://www.valtor-kitchenworks.com/catering-machinery/industrial-kitchens-equipment/tilting-bratt-pan where you can even find a video.

One of the important features of this equipment is the mixing system. We need to give more importance on the keypad and renew all buttons and general design.

Note: On the manual instruction you can find the keypad description. The keys 13, 14 and 15 can be moved. The rest (1-12) must remain on same postion.

Reason: Uploaded dimensions (mm 95x150) and logo

```html
<!DOCTYPE html>
<html lang="en">
<head>
<meta charset="utf-8">
<title>BROVANEL keypad</title>
<link href="https://fonts.googleapis.com/css2?family=Montserrat:wght@800&display=swap" rel="stylesheet">
<style>
  :root {
    --page-bg: #ececec;
    --steel-light: #c9c9c9;
    --steel-mid: #a9a8a6;
    --steel-dark: #8d8c8a;
    --panel-edge: #3a3a3a;
    --brand-magenta: #9c1c67;
    --accent-orange: #ea5b24;
    --key-white: #ffffff;
    --icon-grey: #8c8c8c;
    --display-black: #0b0b0b;
    --segment-edge: #9a9a9a;
  }
  html, body {
    margin: 0;
    width: 1200px;
    height: 900px;
    overflow: hidden;
    background: radial-gradient(circle at 50% 45%, #ffffff 0%, var(--page-bg) 75%);
    font-family: "Montserrat", Arial, sans-serif;
  }
  .keypad {
    position: absolute;
    left: 0;
    top: 0;
    width: 1200px;
    height: 900px;
  }
  .key-label {
    font-family: "Montserrat", Arial, sans-serif;
    font-weight: 800;
    fill: var(--icon-grey);
    text-anchor: middle;
  }
  .brand-name {
    font-family: "Montserrat", Arial, sans-serif;
    font-weight: 800;
    fill: var(--brand-magenta);
    text-anchor: middle;
    letter-spacing: 1px;
  }
  .icon {
    fill: none;
    stroke: var(--icon-grey);
    stroke-width: 2.4;
    stroke-linecap: round;
    stroke-linejoin: round;
  }
  .segment {
    fill: #161616;
    stroke: var(--segment-edge);
    stroke-width: 0.9;
  }
</style>
</head>
<body>
<svg class="keypad" viewBox="0 0 1200 900" xmlns="http://www.w3.org/2000/svg" aria-label="BROVANEL cooker control keypad">
  <defs>
    <linearGradient id="brushed-steel" x1="0" y1="0" x2="1" y2="0">
      <stop offset="0" stop-color="var(--steel-dark)"/>
      <stop offset="0.3" stop-color="var(--steel-mid)"/>
      <stop offset="0.55" stop-color="var(--steel-light)"/>
      <stop offset="0.8" stop-color="var(--steel-mid)"/>
      <stop offset="1" stop-color="var(--steel-dark)"/>
    </linearGradient>
    <symbol id="digit-eight" viewBox="0 0 30 44">
      <polygon class="segment" points="4,0 26,0 22,4 8,4"/>
      <polygon class="segment" points="5,22 8,20 22,20 25,22 22,24 8,24"/>
      <polygon class="segment" points="8,40 22,40 26,44 4,44"/>
      <polygon class="segment" points="2,2 6,6 6,18 2,21"/>
      <polygon class="segment" points="28,2 28,21 24,18 24,6"/>
      <polygon class="segment" points="2,23 6,26 6,38 2,42"/>
      <polygon class="segment" points="28,23 28,42 24,38 24,26"/>
    </symbol>
    <symbol id="thermometer" viewBox="0 0 20 34">
      <path class="icon" d="M7 22 V5 a3 3 0 0 1 6 0 V22 a6 6 0 1 1 -6 0 Z"/>
      <line class="icon" x1="10" y1="10" x2="10" y2="26"/>
      <line class="icon" x1="13" y1="9" x2="16" y2="9"/>
      <line class="icon" x1="13" y1="14" x2="16" y2="14"/>
    </symbol>
  </defs>

  <!-- Panel -->
  <rect x="458" y="224" width="285" height="451" fill="url(#brushed-steel)" stroke="var(--panel-edge)" stroke-width="1"/>

  <!-- Power switch -->
  <rect class="power-key" x="489" y="255" width="91" height="45" rx="9" fill="var(--brand-magenta)" stroke="var(--key-white)" stroke-width="3"/>
  <line x1="534" y1="263" x2="534" y2="292" stroke="var(--key-white)" stroke-width="3" stroke-linecap="round"/>

  <!-- Displays -->
  <rect class="display" x="473" y="313" width="124" height="63" rx="8" fill="var(--display-black)" stroke="var(--key-white)" stroke-width="3"/>
  <use href="#digit-eight" x="484" y="322" width="30" height="44"/>
  <use href="#digit-eight" x="521" y="322" width="30" height="44"/>
  <use href="#digit-eight" x="558" y="322" width="30" height="44"/>

  <rect class="display" x="473" y="380" width="124" height="62" rx="8" fill="var(--display-black)" stroke="var(--key-white)" stroke-width="3"/>
  <use href="#digit-eight" x="484" y="389" width="30" height="44"/>
  <use href="#digit-eight" x="521" y="389" width="30" height="44"/>
  <use href="#digit-eight" x="558" y="389" width="30" height="44"/>

  <!-- Up / down rocker -->
  <rect class="rocker" x="613" y="321" width="47" height="118" rx="16" fill="var(--accent-orange)" stroke="var(--key-white)" stroke-width="3"/>
  <polygon points="636,333 647,353 625,353" fill="none" stroke="var(--key-white)" stroke-width="2.4" stroke-linejoin="round"/>
  <polygon points="636,426 647,406 625,406" fill="none" stroke="var(--key-white)" stroke-width="2.4" stroke-linejoin="round"/>

  <!-- Probe temperature key -->
  <circle cx="636" cy="278" r="24" fill="var(--key-white)"/>
  <use href="#thermometer" x="628" y="262" width="18" height="30"/>
  <line class="icon" x1="622" y1="293" x2="652" y2="268"/>
  <circle cx="652" cy="268" r="2.5" fill="var(--icon-grey)"/>

  <!-- Start / stop -->
  <circle cx="700" cy="278" r="24" fill="var(--key-white)"/>
  <text class="key-label" x="700" y="276" font-size="9">START</text>
  <text class="key-label" x="700" y="287" font-size="9">STOP</text>

  <!-- Temperature -->
  <circle cx="700" cy="345" r="24" fill="var(--key-white)"/>
  <use href="#thermometer" x="691" y="329" width="18" height="31"/>

  <!-- Timer -->
  <circle cx="700" cy="410" r="24" fill="var(--key-white)"/>
  <circle class="icon" cx="700" cy="410" r="14" stroke-width="1.8"/>
  <polyline class="icon" points="700,400 700,410 707,414" stroke-width="1.8"/>

  <!-- Clockwise rotation -->
  <circle cx="511" cy="490" r="24" fill="var(--key-white)"/>
  <path class="icon" d="M497 492 A15 15 0 0 1 525 488"/>
  <polyline class="icon" points="520,485 525,491 529,484"/>

  <!-- Counter-clockwise rotation -->
  <circle cx="573" cy="490" r="24" fill="var(--key-white)"/>
  <path class="icon" d="M587 492 A15 15 0 0 0 559 488"/>
  <polyline class="icon" points="564,485 559,491 555,484"/>

  <!-- Mixer on/off -->
  <circle cx="636" cy="490" r="24" fill="var(--key-white)"/>
  <text class="key-label" x="636" y="488" font-size="9">MIXER</text>
  <text class="key-label" x="636" y="499" font-size="8.5">ON/OFF</text>

  <!-- Continuous mixing -->
  <circle cx="700" cy="490" r="24" fill="var(--key-white)"/>
  <path class="icon" d="M693 478 A13 13 0 1 0 709 480" stroke-width="3.6"/>
  <polyline class="icon" points="703,474 709,480 704,486" stroke-width="2.6"/>

  <!-- Intermittent mixing -->
  <circle cx="511" cy="573" r="24" fill="var(--key-white)"/>
  <polyline class="icon" points="498,578 504,566 510,580 516,567 520,575 524,570"/>

  <!-- Reset -->
  <circle cx="573" cy="573" r="24" fill="var(--key-white)"/>
  <text class="key-label" x="573" y="577" font-size="9">RESET</text>

  <!-- Speed knob -->
  <path d="M648 580 A33 33 0 0 1 641 538" fill="none" stroke="var(--accent-orange)" stroke-width="6"/>
  <path d="M643 533 A33 33 0 0 1 667 522" fill="none" stroke="var(--accent-orange)" stroke-width="6"/>
  <path d="M671 522 A33 33 0 0 1 697 541" fill="none" stroke="var(--accent-orange)" stroke-width="6"/>
  <path d="M699 546 A33 33 0 0 1 688 580" fill="none" stroke="var(--accent-orange)" stroke-width="6"/>
  <circle class="knob" cx="667" cy="555" r="26" fill="var(--display-black)"/>

  <!-- Brand name -->
  <text class="brand-name" x="600" y="652" font-size="30">BROVANEL</text>
</svg>
</body>
</html>
```